'Lanterns' CD cover project

I am recording a new album 'Lanterns' and need a CD cover design. No design specs, but I want something simple and classy. My name (Marek Townley) does not necessarily have to appear on the cover, and it does not have to relate to my previous 11 albums. I have posted some of my own ideas on Snapwall.

Target Market(s)

I have an established 50s+ fan base, but am seeking to appeal to a younger more modern audience.

Font styles to use
Other font styles liked:
• Yu Gothic Light but open to suggestions.

Colors

Designer to choose colors to be used in the design.

Requirements
Must have
• Simple, clean, classy, Im open to a photo image or simply a graphic design.
Nice to have
• Modern (pastel?) colors.. if pastels are modern?!
Should not have
• Nothing 'In Yer Face'. Prefer sublte, nuance, classy, tasteful, clean lines, unusual font.

```html
<!DOCTYPE html>
<html lang="en">
<head>
<meta charset="UTF-8">
<title>Lanterns — Album Cover</title>
<link rel="stylesheet" href="https://fonts.googleapis.com/css2?family=Cormorant+Garamond:wght@400&display=swap">
<style>
  :root {
    --page: #ffffff;
    --sky-top: #e3d2b4;
    --sky-light: #f1e1b9;
    --haze: #c2a776;
    --haze-dark: #9c8259;
    --water-light: #b39a70;
    --water-mid: #8d7552;
    --water-dark: #4a3b28;
    --band: rgba(196, 186, 172, 0.55);
    --title: #f3f4fb;
  }
  html, body {
    margin: 0;
    padding: 0;
    width: 1200px;
    height: 1200px;
    overflow: hidden;
    background: var(--page);
  }
  .canvas {
    position: relative;
    width: 1200px;
    height: 1200px;
    background: var(--page);
  }
  .cover {
    position: absolute;
    left: 150px;
    top: 100px;
    width: 904px;
    height: 824px;
    overflow: hidden;
  }
  .cover-photo {
    position: absolute;
    inset: 0;
    background:
      linear-gradient(to right, rgba(255, 255, 255, 0.08), rgba(70, 62, 55, 0.22)),
      linear-gradient(to bottom,
        var(--sky-top) 0%,
        var(--sky-light) 30%,
        #e8d3a4 44%,
        var(--haze) 52%,
        var(--haze-dark) 60%,
        #bfa985 68%,
        var(--water-light) 78%,
        var(--water-mid) 90%,
        var(--water-dark) 100%);
  }
  .title-band {
    position: absolute;
    left: 0;
    right: 0;
    top: 456px;
    height: 162px;
    background: var(--band);
    display: flex;
    align-items: center;
    justify-content: center;
  }
  .album-title {
    margin: 0;
    font-family: "Cormorant Garamond", "Times New Roman", serif;
    font-weight: 400;
    font-size: 130px;
    line-height: 1;
    letter-spacing: 0.1em;
    padding-left: 0.1em;
    color: var(--title);
    text-transform: uppercase;
  }
</style>
</head>
<body>
  <main class="canvas">
    <section class="cover">
      <div class="cover-photo" role="img" aria-label="Photograph of a misty river at sunrise with a hazy treeline reflected in calm water"></div>
      <div class="title-band">
        <h1 class="album-title">Lanterns</h1>
      </div>
    </section>
  </main>
</body>
</html>
```